DJ company new brochure of services offered

I would like to get a new price sheet made for my company services. Currently it's text only. I would like to add pictures next to each service description also like to add general background colors, and just make it look more attractive overall.

Uplighting - File #4 & file #10
Centerpiece pin-spots - File #15
Wedding Cake Spot - file #13 (can you crop out the logo at the bottom)?
Dance Floor Decal File #5
Gobo Monogram - File # 3
market lighting - file #14
ballroom draping - file #7
Video/projections screens: File #13
Indoor safe sparkler effect (not listed on price sheet yet) File #11
Dancing on a cloud - File #9
Co2 Cannons - File #6

Target Market(s)

bride and grooms

Industry/Entity Type

Entertainment

Font styles to use
Serif

Colors

Designer to choose colors to be used in the design.

Requirements
Must have
• my website is www.brightloomevents.example
• instagram is: @brightloomevents.example

```html
<!DOCTYPE html>
<html lang="en">
<head>
<meta charset="utf-8">
<title>Brightloom Events – Wedding Price Sheet</title>
<link rel="stylesheet" href="https://fonts.googleapis.com/css2?family=Ubuntu:ital,wght@0,400;0,500;0,700;1,400&family=Open+Sans:ital,wght@0,300;0,400;0,600;1,400&display=swap">
<style>
:root{
  --canvas:#e7e7e7;
  --navy:#0c1330;
  --navy-deep:#070b1e;
  --royal:#1c2d8c;
  --ink:#1d2a6b;
  --red:#e8262b;
  --white:#ffffff;
  --muted:#b9bccb;
  --grey-text:#6e6f75;
  --footer:#4a4b50;
  --side:#7b7c82;
  --band:#1e1f24;
}
*{box-sizing:border-box;margin:0;padding:0}
html,body{width:1200px;height:750px;overflow:hidden;background:var(--canvas)}
body{position:relative;font-family:"Open Sans",sans-serif}
.abs{position:absolute}
.page{position:absolute;top:42px;width:527px;height:673px;overflow:hidden;box-shadow:0 4px 14px rgba(0,0,0,.18)}

/* ---------- Front page ---------- */
.front{left:59px;background:radial-gradient(ellipse 75% 60% at 50% 18%,#2f49c4 0%,var(--royal) 30%,#121c5a 60%,var(--navy) 100%)}
.front .dome{left:-60px;top:205px;width:647px;height:520px;border-radius:50% 50% 0 0/38% 38% 0 0;background:radial-gradient(ellipse at 50% 30%,#151a3a 0%,var(--navy-deep) 70%)}
.brand{left:0;width:100%;top:70px;display:flex;justify-content:center;align-items:center;gap:8px}
.brand .dot{width:14px;height:14px;border-radius:50%;background:var(--red)}
.brand .name{font-family:"Ubuntu",sans-serif;font-weight:400;font-size:26px;color:var(--red);letter-spacing:.5px}
.services-line{left:0;width:100%;top:143px;text-align:center;font-family:"Ubuntu",sans-serif;font-weight:500;font-size:18px;color:var(--white)}
.package-title{left:0;width:100%;top:203px;text-align:center;font-family:"Ubuntu",sans-serif;font-weight:700;font-size:16px;color:var(--white)}
.package-sub{left:0;width:100%;top:229px;text-align:center;font-style:italic;font-size:13px;color:var(--muted)}
.includes{left:62px;top:272px;list-style:none}
.includes li{display:flex;align-items:center;height:18.6px;font-size:12.3px;font-weight:300;color:var(--white)}
.includes svg{width:13px;height:13px;margin-right:14px;flex:none}
.rates{left:390px;top:286px;width:110px}
.rates div{display:flex;justify-content:flex-end;align-items:baseline;gap:7px;height:21px}
.rates .day{font-style:italic;font-size:9.5px;color:var(--white)}
.rates .amt{font-family:"Ubuntu",sans-serif;font-weight:500;font-size:14.5px;color:var(--red)}
.front-photo{left:0;top:410px;width:100%;height:206px;background:linear-gradient(180deg,rgba(7,11,30,0) 0%,#2a3570 30%,#4a5a8c 55%,#1c2444 85%,#0d1226 100%)}
.extras{left:71px;top:510px;width:384px;height:95px;border-radius:8px;background:rgba(16,20,42,.82);text-align:center}
.extras h3{font-family:"Ubuntu",sans-serif;font-weight:500;font-size:14px;color:var(--red);margin-top:8px}
.extras p{font-size:8.5px;font-weight:300;color:var(--muted);margin-top:2px}
.extras h3+p+h3{margin-top:14px}
.front-footer{left:0;bottom:0;width:100%;height:58px;background:var(--footer);display:flex;align-items:center;justify-content:center;font-size:11.5px;font-weight:600;color:var(--white);gap:7px}

/* ---------- Back page ---------- */
.back{left:610px;background:var(--side)}
.back-photo{left:0;top:0;width:100%;height:280px;background:linear-gradient(100deg,#3b2a55 0%,#8a6fb8 25%,#c9a98a 50%,#b48ccf 75%,#5d4c86 100%)}
.arch{left:25px;top:102px;width:475px;height:410px;background:var(--white);border-radius:50% 50% 0 0/36% 36% 0 0}
.addon-title{left:25px;width:475px;top:147px;text-align:center;font-family:"Ubuntu",sans-serif;font-weight:700;font-size:17px;color:var(--ink)}
.addon-sub{left:25px;width:475px;top:171px;text-align:center;font-style:italic;font-size:10px;color:var(--grey-text)}
.thumb{left:82px;width:54px;border:2px solid #d9d9de}
.svc{left:150px;width:310px}
.svc .name{font-family:"Ubuntu",sans-serif;font-weight:700;font-size:12px;color:var(--ink)}
.svc .name i{font-family:"Open Sans",sans-serif;font-weight:400;font-size:8.5px}
.svc .note{font-style:italic;font-size:8.5px;color:var(--ink)}
.row{display:flex;align-items:baseline;font-size:8.5px;font-weight:300;color:var(--grey-text);height:14.5px}
.row .lead{flex:1;border-bottom:1px dotted #999;margin:0 2px;transform:translateY(-2px)}
.price{width:78px;font-family:"Ubuntu",sans-serif;font-weight:700;font-size:13px;color:var(--ink)}
.small{font-style:italic;font-size:7px;color:var(--grey-text);line-height:1}
.back-band{left:0;top:510px;width:100%;height:12px;background:var(--band)}
.back-footer{left:0;top:522px;width:100%;height:151px;background:var(--footer)}
.back-footer .edge{top:0;width:25px;height:100%;background:#3f4045}
.back-brand{left:62px;top:568px;display:flex;align-items:center;gap:7px}
.back-brand .dot{width:12px;height:12px;border-radius:50%;background:var(--red)}
.back-brand .name{font-family:"Ubuntu",sans-serif;font-size:21px;color:var(--red)}
.contact{left:220px;width:244px;top:538px;text-align:center;color:var(--white)}
.contact .intro{font-style:italic;font-size:10px;font-weight:300;line-height:15px}
.contact .info{margin-top:12px;font-weight:600;font-size:9.5px;line-height:14.6px}
</style>
</head>
<body>

<section class="page front">
  <div class="abs dome"></div>
  <div class="abs brand"><span class="dot"></span><span class="name">Brightloom Events</span></div>
  <div class="abs services-line">DJs | Lighting | Pro Audio | Visual</div>
  <h2 class="abs package-title">5-hour DJ/MC Wedding Reception Package:</h2>
  <div class="abs package-sub">This package includes:</div>
  <ul class="abs includes">
    <li><svg viewBox="0 0 10 10"><path d="M5 0L6.2 3.6 10 3.8 7 6.1 8 10 5 7.7 2 10 3 6.1 0 3.8 3.8 3.6Z" fill="#e8262b"/></svg>Formally attired &amp; live mixing DJ</li>
    <li><svg viewBox="0 0 10 10"><path d="M5 0L6.2 3.6 10 3.8 7 6.1 8 10 5 7.7 2 10 3 6.1 0 3.8 3.8 3.6Z" fill="#e8262b"/></svg>Emcee hosting all announcements</li>
    <li><svg viewBox="0 0 10 10"><path d="M5 0L6.2 3.6 10 3.8 7 6.1 8 10 5 7.7 2 10 3 6.1 0 3.8 3.8 3.6Z" fill="#e8262b"/></svg>Powered Speaker Sound System</li>
    <li><svg viewBox="0 0 10 10"><path d="M5 0L6.2 3.6 10 3.8 7 6.1 8 10 5 7.7 2 10 3 6.1 0 3.8 3.8 3.6Z" fill="#e8262b"/></svg>Wireless Microphone for toasts, speeches</li>
    <li><svg viewBox="0 0 10 10"><path d="M5 0L6.2 3.6 10 3.8 7 6.1 8 10 5 7.7 2 10 3 6.1 0 3.8 3.8 3.6Z" fill="#e8262b"/></svg>In-person consultation to discuss event details</li>
    <li><svg viewBox="0 0 10 10"><path d="M5 0L6.2 3.6 10 3.8 7 6.1 8 10 5 7.7 2 10 3 6.1 0 3.8 3.8 3.6Z" fill="#e8262b"/></svg>Online access to planning forms and music database</li>
    <li><svg viewBox="0 0 10 10"><path d="M5 0L6.2 3.6 10 3.8 7 6.1 8 10 5 7.7 2 10 3 6.1 0 3.8 3.8 3.6Z" fill="#e8262b"/></svg>Up to 6 hours of continuous entertainment</li>
  </ul>
  <div class="abs rates">
    <div><span class="day">Saturday</span><span class="amt">$1495</span></div>
    <div><span class="day">Fri &amp; Sun</span><span class="amt">$1395</span></div>
    <div><span class="day">Mon - Th</span><span class="amt">$1295</span></div>
  </div>
  <div class="abs front-photo" role="img" aria-label="Photo of a couple's first dance on a fog-covered floor in a lit ballroom"></div>
  <div class="abs extras">
    <h3>Ceremony music Included</h3>
    <p>(includes sound equipment, wireless mic and ceremony music)</p>
    <h3>Cocktail Hour Music Included</h3>
    <p>(includes music in cocktail hour area)</p>
  </div>
  <footer class="abs front-footer">
    <span>www.brightloomevents.example</span><span>|</span><span>555.014.2290</span><span>|</span><span>hello@brightloomevents.example</span>
  </footer>
</section>

<section class="page back">
  <div class="abs back-photo" role="img" aria-label="Photo collage of a cold-spark cannon effect and a couple dancing in a draped, uplit ballroom"></div>
  <div class="abs arch"></div>
  <h2 class="abs addon-title">Additional Service Add-on:</h2>
  <div class="abs addon-sub">(when booked with DJ package)</div>

  <div class="abs thumb" style="top:210px;height:53px;background:linear-gradient(135deg,#d8c7ef,#8f74c6)" role="img" aria-label="Photo of a ballroom with purple uplighting"></div>
  <div class="abs svc" style="top:207px">
    <div class="name">Room Up-Lighting</div>
    <div class="note">(color of your choice)</div>
    <div class="row"><span>- 20 fixtures (med-large room)</span><span class="lead"></span><span class="price">$400</span></div>
    <div class="row"><span>- 16 fixtures (med-large room)</span><span class="lead"></span><span class="price">$350</span></div>
    <div class="row"><span>- 12 fixtures (small-med room)</span><span class="lead"></span><span class="price">$300</span></div>
  </div>

  <div class="abs thumb" style="top:291px;height:41px;background:linear-gradient(135deg,#6b4a35,#d7a774)" role="img" aria-label="Photo of pin-spotted table centerpieces"></div>
  <div class="abs svc" style="top:289px">
    <div class="name">Pin Spot Lighting</div>
    <div class="row"><span>- Wedding Cake/Centerpieces/</span><span class="lead"></span><span class="price">$30+</span></div>
    <div class="row"><span>Sweetheart Table/etc.</span></div>
  </div>

  <div class="abs thumb" style="top:340px;height:32px;background:linear-gradient(135deg,#b493e6,#6a3fb4)" role="img" aria-label="Photo of a monogram decal on a dance floor"></div>
  <div class="abs svc" style="top:343px">
    <div class="name">Dance Floor Decal/Gobo Monogram</div>
    <div class="row"><span>- B&amp;G names appear onto wall or dance floor</span><span class="lead"></span><span class="price">$250+</span></div>
  </div>

  <div class="abs thumb" style="top:378px;height:32px;background:linear-gradient(135deg,#3d2f28,#b99069)" role="img" aria-label="Photo of a lit dance floor in a reception hall"></div>
  <div class="abs svc" style="top:384px">
    <div class="row"><span class="name">Dance Floor Lighting</span><span class="lead"></span><span class="price">$200+</span></div>
  </div>
  <div class="abs small" style="left:382px;top:398px">(depending on style)</div>

  <div class="abs svc" style="top:408px">
    <div class="row"><span class="name">White Dance Floor <i>(Square or Round)</i></span><span class="lead"></span><span class="price">$1000+</span></div>
  </div>
  <div class="abs small" style="left:382px;top:424px">(seamless only)</div>

  <div class="abs thumb" style="top:417px;height:32px;background:linear-gradient(135deg,#e06fc4,#8c2f9c)" role="img" aria-label="Photo of a projection screen at an event"></div>
  <div class="abs svc" style="top:433px">
    <div class="row"><span class="name">A/V <i>(Screens, Projectors, Video Display)</i></span><span class="lead"></span><span class="price">$200+</span></div>
  </div>

  <div class="abs thumb" style="top:456px;height:32px;background:linear-gradient(135deg,#4c4a4c,#c8b9a2)" role="img" aria-label="Photo of string bistro lights over a tent"></div>
  <div class="abs svc" style="top:464px">
    <div class="row"><span class="name">String/Bistro Lighting</span><span class="lead"></span><span class="price"></span></div>
  </div>
  <div class="abs small" style="left:382px;top:469px">depends on size<br>- contact us</div>

  <div class="abs back-band"></div>
  <div class="abs back-footer">
    <div class="abs edge" style="left:0"></div>
    <div class="abs edge" style="right:0"></div>
  </div>
  <div class="abs back-brand"><span class="dot"></span><span class="name">Brightloom Events</span></div>
  <div class="abs contact">
    <div class="intro">* We offer a wide range of additional services.<br>Please contact us for more info &amp; pricing.</div>
    <div class="info">DJs | Lighting | Pro Audio | Visual<br>555.014.2290<br>hello@brightloomevents.example<br>www.brightloomevents.example</div>
  </div>
</section>

</body>
</html>
```